***Dozing Heron Lash Studio is in need of a web site makeover***

I need a makeover for my existing web site. www.dozing-heron.example

Please help!!!! Thanks 😁

Dozing Heron Lash Studio is an eyelash extension salon. In addition, we also provide skincare services (facials, waxing, etc). Our web site needs to appear professional and intuitive. In addition, allowing for ease of online booking is of utmost importance.

The client web site experience:
- esthetically pleasing and makes sense
- clearly recognize brand (Dozing Heron)
- easy to follow web pages
- easy to book appointments online
- easy to sign up for email updates
- easily locate services menu and pricing

Target Market(s)

Dozing Heron Lash Studio offers eyelash extension services, as well as various skincare services (I.e. facials, waxing, etc.)

Industry/Entity Type

Beauty Salon

Number of Pages Required

5+ page

Font styles to use
Sans Serif
Script

Colors
000000
fee3d5
eaeaea
ffffff

Requirements
Must have
• - Home page with static contact information
• - Services page (menu of services and pricing)
• - Photo gallery page
• - Contact page
• - Q&A page
Nice to have
• Professional, classy, intuitive and simple for clients to be able to book online.

```html
<!DOCTYPE html>
<html lang="en">
<head>
<meta charset="utf-8">
<title>Dozing Heron Lash Studio</title>
<link rel="stylesheet" href="https://fonts.googleapis.com/css2?family=Great+Vibes&family=Open+Sans:wght@400;600;700&display=swap">
<style>
:root{
  --pink:#e0337f;
  --pink-bar:#f06ba0;
  --pink-soft:#f9d2e2;
  --pink-mid:#f5bcd3;
  --peach:#fee3d5;
  --grey:#eaeaea;
  --white:#ffffff;
  --ink:#555555;
  --footer-a:#6e0936;
  --footer-b:#c2185b;
}
*{box-sizing:border-box;margin:0;padding:0}
html,body{width:1200px;height:2880px;overflow:hidden}
body{background:var(--white);font-family:"Open Sans",Arial,sans-serif;color:var(--ink)}
.page{width:1200px;height:2880px;position:relative}

/* header */
.site-header{height:140px;position:relative}
.brand{position:absolute;left:0;right:0;top:40px;text-align:center;font-family:"Open Sans",Arial,sans-serif;font-weight:600;color:var(--pink);font-size:30px;line-height:36px}
.header-tools{position:absolute;right:70px;top:22px;display:flex;align-items:center;gap:8px}
.social-dot{width:22px;height:22px;border-radius:50%;background:var(--pink)}
.book-link{margin-left:28px;font-family:"Great Vibes",cursive;color:var(--pink);font-size:20px}
.main-nav{position:absolute;left:70px;right:70px;top:102px;height:34px;border-top:2px solid var(--pink-soft);border-bottom:2px solid var(--pink-soft);display:flex;align-items:center;justify-content:space-between;padding:0 6px}
.main-nav a{font-family:"Great Vibes",cursive;color:var(--pink);font-size:19px;text-decoration:none}
.main-nav a.current{color:#222;border-bottom:2px solid var(--pink)}
.main-nav .sep{width:1px;height:18px;background:var(--pink-mid)}

/* hero */
.hero{height:540px;position:relative}
.hero-slide{position:absolute;left:70px;right:70px;top:4px;height:505px;border:3px solid var(--pink);background:linear-gradient(100deg,#f3c6d9 0%,#a9b9d6 22%,#6f7fb0 38%,#c79ad0 55%,#f4e3ec 68%,#5b2a8c 80%,#3a1a66 100%)}
.hero-arrow{position:absolute;top:242px}
.hero-arrow.left{left:88px}.hero-arrow.right{right:88px}
.hero-dots{position:absolute;top:522px;left:0;right:0;display:flex;justify-content:center;gap:8px}
.hero-dots span{width:8px;height:8px;border-radius:50%;background:var(--pink-mid)}
.hero-dots span.on{background:var(--pink)}

/* sections */
.section{position:relative;text-align:center}
.section-title{font-family:"Great Vibes",cursive;color:var(--pink);font-size:40px;line-height:48px;font-weight:400}
.section-text{width:1020px;margin:0 auto;font-size:14px;line-height:21px;color:var(--ink)}
.btn-outline{display:inline-block;border:2px solid var(--pink);border-radius:4px;background:var(--white);color:var(--pink);font-size:13px;font-weight:600;letter-spacing:1px;padding:6px 20px;text-transform:uppercase}
.about{height:300px;background:var(--peach);padding-top:36px}
.about .section-text{margin-top:16px}
.about .btn-outline{margin-top:20px}

.lash{height:380px;background:var(--white);padding-top:16px}
.skin{height:380px;background:var(--pink-soft);padding-top:22px}
.card-row{display:flex;justify-content:center;gap:20px;margin-top:12px}
.card{width:336px;border:2px solid var(--pink-bar);background:var(--white)}
.card-photo{height:180px}
.skin .card-photo{height:165px}
.photo-eye{background:linear-gradient(180deg,#8a5a3c 0%,#e9c1a6 35%,#f3d4c1 70%,#e7b59d 100%)}
.photo-spa{background:linear-gradient(135deg,#e9efe6 0%,#f3e6dc 45%,#d9c7b8 75%,#b9d7b0 100%)}
.card-caption{height:26px;background:var(--pink-bar);color:var(--white);font-family:"Great Vibes",cursive;font-size:19px;line-height:26px}
.lash .btn-outline,.skin .btn-outline{margin-top:18px}

.gallery{height:380px;background:var(--pink-mid);padding-top:22px}
.gallery-row{display:flex;justify-content:center;gap:18px;margin-top:14px;position:relative}
.gallery-item{width:176px;background:var(--white);padding:4px}
.gallery-photo{height:160px;background:linear-gradient(180deg,#7a4a32 0%,#e6b89d 40%,#f2d2bf 75%,#e0a891 100%)}
.gallery-caption{background:var(--pink);color:var(--white);text-align:left;padding:4px 8px;font-size:11px;line-height:14px}
.gallery-caption b{display:block;font-size:12px}
.gallery-arrow{position:absolute;top:90px}
.gallery-arrow.left{left:66px}.gallery-arrow.right{right:66px}
.gallery .btn-outline{margin-top:22px}

.faq{height:240px;background:var(--pink-soft);padding-top:22px}
.faq .section-text{margin-top:12px}
.faq .btn-outline{margin-top:14px}

/* booking */
.booking{height:360px;background:var(--pink-mid);padding-top:12px}
.booking-card{width:1040px;margin:8px auto 0;border:2px solid var(--pink);background:var(--white);text-align:left;height:282px;position:relative}
.tabs{display:flex;height:34px;background:var(--grey)}
.tab{padding:0 26px;font-size:13px;line-height:34px;color:#444;font-weight:600;border-right:1px solid #d0d0d0}
.tab.active{background:var(--pink);color:var(--white)}
.form-grid{display:grid;grid-template-columns:1fr 1fr 1fr;gap:16px 22px;padding:26px 26px 0}
.field{border-bottom:1px solid #cfcfcf;height:34px;font-size:12px;line-height:34px;color:#777;padding:0 8px;display:flex;justify-content:space-between;align-items:center}
.field.message{grid-row:span 2;height:84px;border:1px solid #cfcfcf;align-items:flex-start;line-height:28px}
.form-actions{position:absolute;right:26px;bottom:40px;display:flex;gap:14px}
.btn-solid{width:120px;height:30px;line-height:30px;text-align:center;color:var(--white);font-size:13px;font-weight:700;letter-spacing:1px}
.btn-submit{background:var(--pink)}
.btn-reset{background:#9a9a9a}

/* footer */
.site-footer{height:160px;background:linear-gradient(180deg,var(--footer-a),var(--footer-b));color:var(--white);position:relative}
.footer-brand{position:absolute;left:70px;top:34px;font-family:"Open Sans",Arial,sans-serif;font-weight:600;font-size:20px;line-height:26px;color:var(--pink-mid)}
.footer-col{position:absolute;top:30px;font-size:12px;line-height:18px}
.footer-col h4{font-size:13px;font-weight:700;margin-bottom:4px}
.footer-col.links{left:340px}.footer-col.links2{left:530px;top:52px}.footer-col.contact{left:690px}
.footer-social{position:absolute;right:70px;top:32px;display:flex;gap:8px}
.footer-social span{width:26px;height:26px;border-radius:50%;border:2px solid var(--white)}
.copyright{position:absolute;right:70px;top:74px;font-size:11px;line-height:16px;text-align:left;width:190px}
</style>
</head>
<body>
<div class="page">

<header class="site-header">
  <div class="brand">Dozing Heron Lash Studio</div>
  <div class="header-tools">
    <span class="social-dot"></span><span class="social-dot"></span><span class="social-dot"></span><span class="social-dot"></span>
    <span class="book-link">Book Appointment</span>
  </div>
  <nav class="main-nav">
    <a class="current">Home</a><span class="sep"></span>
    <a>About Us</a><span class="sep"></span>
    <a>Eyelash Extension Services</a><span class="sep"></span>
    <a>Skincare Services</a><span class="sep"></span>
    <a>Photo Gallery</a><span class="sep"></span>
    <a>FAQs</a><span class="sep"></span>
    <a>Contact</a>
  </nav>
</header>

<section class="hero">
  <div class="hero-slide" role="img" aria-label="Close-up of an eye with long lash extensions beside a purple flower"></div>
  <svg class="hero-arrow left" width="16" height="28" viewBox="0 0 16 28"><path d="M14 2 L2 14 L14 26" fill="none" stroke="#fff" stroke-width="3"/></svg>
  <svg class="hero-arrow right" width="16" height="28" viewBox="0 0 16 28"><path d="M2 2 L14 14 L2 26" fill="none" stroke="#fff" stroke-width="3"/></svg>
  <div class="hero-dots"><span class="on"></span><span></span><span></span><span></span></div>
</section>

<section class="section about">
  <h2 class="section-title">About Dozing Heron Lash Studio</h2>
  <p class="section-text">Dozing Heron Lash Studio is a calm, welcoming space for beautiful lashes and healthy skin. Our certified stylists craft custom eyelash extensions that suit your eye shape, lifestyle and look. We also offer facials, waxing and body treatments using gentle, quality products. Book online in minutes, relax in our cozy studio, and leave feeling refreshed, confident and ready to be seen.</p>
  <span class="btn-outline">Read More</span>
</section>

<section class="section lash">
  <h2 class="section-title">Eyelash Extension Services</h2>
  <div class="card-row">
    <div class="card"><div class="card-photo photo-eye" role="img" aria-label="Eye with classic lash extensions"></div><div class="card-caption">Eyelash Extension #1</div></div>
    <div class="card"><div class="card-photo photo-eye" role="img" aria-label="Eye with volume lash extensions"></div><div class="card-caption">Eyelash Extension #2</div></div>
    <div class="card"><div class="card-photo photo-eye" role="img" aria-label="Eye with hybrid lash extensions"></div><div class="card-caption">Eyelash Extension #3</div></div>
  </div>
  <span class="btn-outline">Discover More</span>
</section>

<section class="section skin">
  <h2 class="section-title">Skincare Services</h2>
  <div class="card-row">
    <div class="card"><div class="card-photo photo-spa" role="img" aria-label="Client receiving a facial mask"></div><div class="card-caption">Facial</div></div>
    <div class="card"><div class="card-photo photo-spa" role="img" aria-label="Waxing treatment at the spa"></div><div class="card-caption">Waxing</div></div>
    <div class="card"><div class="card-photo photo-spa" role="img" aria-label="Relaxing body spa treatment"></div><div class="card-caption">Body Spa</div></div>
  </div>
  <span class="btn-outline">Discover More</span>
</section>

<section class="section gallery">
  <h2 class="section-title">Photo Gallery</h2>
  <div class="gallery-row">
    <svg class="gallery-arrow left" width="12" height="22" viewBox="0 0 12 22"><path d="M10 2 L2 11 L10 20" fill="none" stroke="#fff" stroke-width="3"/></svg>
    <div class="gallery-item"><div class="gallery-photo" role="img" aria-label="Lash extension result photo"></div><div class="gallery-caption"><b>Image 1</b>Classic set</div></div>
    <div class="gallery-item"><div class="gallery-photo" role="img" aria-label="Lash extension result photo"></div><div class="gallery-caption"><b>Image 2</b>Classic set</div></div>
    <div class="gallery-item"><div class="gallery-photo" role="img" aria-label="Lash extension result photo"></div><div class="gallery-caption"><b>Image 3</b>Classic set</div></div>
    <div class="gallery-item"><div class="gallery-photo" role="img" aria-label="Lash extension result photo"></div><div class="gallery-caption"><b>Image 4</b>Classic set</div></div>
    <div class="gallery-item"><div class="gallery-photo" role="img" aria-label="Lash extension result photo"></div><div class="gallery-caption"><b>Image 5</b>Classic set</div></div>
    <svg class="gallery-arrow right" width="12" height="22" viewBox="0 0 12 22"><path d="M2 2 L10 11 L2 20" fill="none" stroke="#fff" stroke-width="3"/></svg>
  </div>
  <span class="btn-outline">View All</span>
</section>

<section class="section faq">
  <h2 class="section-title">Frequently Asked Questions</h2>
  <p class="section-text">Have a question before your visit? Find answers about lash fills, aftercare, appointment length, pricing, deposits and our cancellation policy. Learn how to prepare for your first set, how long extensions last and which skincare treatments suit your skin type. Still unsure? Our friendly team is happy to help by phone or email.</p>
  <span class="btn-outline">Read More</span>
</section>

<section class="section booking">
  <h2 class="section-title">Book an Appointment</h2>
  <div class="booking-card">
    <div class="tabs">
      <span class="tab active">SERVICES</span>
      <span class="tab">Eyelash Extension</span>
      <span class="tab">Skincare Service</span>
    </div>
    <div class="form-grid">
      <div class="field">First Name</div>
      <div class="field">Email</div>
      <div class="field message">Message / Comment</div>
      <div class="field">Last Name</div>
      <div class="field">Desired Date
        <svg width="16" height="16" viewBox="0 0 16 16"><rect x="1" y="3" width="14" height="12" fill="none" stroke="#777" stroke-width="1.5"/><line x1="1" y1="7" x2="15" y2="7" stroke="#777" stroke-width="1.5"/><line x1="5" y1="1" x2="5" y2="5" stroke="#777" stroke-width="1.5"/><line x1="11" y1="1" x2="11" y2="5" stroke="#777" stroke-width="1.5"/></svg>
      </div>
      <div class="field">Phone Number</div>
      <div class="field">Desired Time</div>
    </div>
    <div class="form-actions">
      <span class="btn-solid btn-submit">SUBMIT</span>
      <span class="btn-solid btn-reset">RESET</span>
    </div>
  </div>
</section>

<footer class="site-footer">
  <div class="footer-brand">Dozing Heron Lash Studio</div>
  <div class="footer-col links">
    <h4>Quick Links</h4>
    Home<br>About Us<br>Eyelash Extension Services<br>Skincare Services
  </div>
  <div class="footer-col links2">Photo Gallery<br>FAQs<br>Contact</div>
  <div class="footer-col contact">
    <h4>Contact</h4>
    Address: 12 Willow Lane<br>Phone: 555-0142<br>Email: hello@dozing-heron.example
  </div>
  <div class="footer-social"><span></span><span></span><span></span><span></span></div>
  <div class="copyright">© 2024 Dozing Heron Lash Studio.<br>All rights reserved.</div>
</footer>

</div>
</body>
</html>
```